Design 5 colour schemes for one web page

We are looking for 5 different colour schemes for our product template to create different kinds of colour tone for our web page, it doesn't need to be restructure the layout, just need to provide different color solution.

Please refer to the attached images and take note of the following when you’re working on the design:
(1) Please precisely reproduce the layout. Cannot remove or delete any wordings, components or column shown in the images.
(2) Okay to revise icons, background color or text style as you prefer. But cannot move/delete them.
(3) Provide PSD source files with good layer management. HTML/CSS are not required.
(4) Make reasonable and professional design.

After completion, please send back:
(1) 5 images with 5 different colour schemes.
(2) Related PSD files.

Font styles to use
Serif
Sans Serif

Requirements
Must have
• (1) 5 images for the colour schemes.
• (2) 5 PSD source files with good layer management.
Nice to have
• (1) Explanation about your design of the colour schemes.
Should not have
• (1) HTML/CSS code are not required.

```html
<!DOCTYPE html>
<html lang="en">
<head>
<meta charset="utf-8">
<title>Sports Betting</title>
<link href="https://fonts.googleapis.com/css2?family=Arimo:wght@400;700&display=swap" rel="stylesheet">
<style>
:root{
  --ink:#1f2a2e;
  --topbar:#142127;
  --navbar:#1f3239;
  --brand:#0f5566;
  --brand-dark:#0a3d4a;
  --brand-mid:#2b7384;
  --brand-line:#4a8d9c;
  --row:#e3ecee;
  --row-alt:#ecf2f3;
  --time-cell:#d5e1e4;
  --cell-line:#ffffff;
  --panel-gray:#dde6e8;
  --accent:#f0a21a;
  --blue:#1479b8;
  --red:#cc2a1f;
  --home:#4b5a5e;
  --away:#0f5566;
  --muted:#7d8b8f;
}
*{box-sizing:border-box;margin:0;padding:0}
html,body{width:1065px;height:1200px;overflow:hidden;background:#fff}
body{font-family:"Arimo",Arial,sans-serif;color:var(--ink)}
.canvas{position:relative;width:1168px;height:1316px;transform:scale(0.91182);transform-origin:0 0;background:#fff}
.abs{position:absolute}

/* top bar */
.topbar{left:0;top:0;width:1168px;height:38px;background:var(--topbar);color:#fff;font-size:14px}
.topbar .menu{left:99px;top:8px;display:flex;gap:12px;align-items:center}
.badge{background:var(--accent);color:var(--topbar);font-weight:700;border-radius:4px;padding:1px 7px;font-size:13px}
.topbar .user{left:763px;top:10px}
.wallet{left:848px;top:4px;width:154px;height:27px;border:1px solid var(--brand-line);padding:5px 6px}
.signout{left:1009px;top:4px;width:92px;height:27px;border:1px solid var(--brand-line);padding:5px 12px}

/* header */
.logo{left:100px;top:60px;font-size:56px;color:var(--brand);letter-spacing:1px}
.results{left:1018px;top:60px;font-size:14px;display:flex;align-items:center;gap:8px}
.sports-tab{left:350px;top:88px;width:122px;height:47px;background:var(--brand);color:#fff;font-size:24px;text-align:center;padding-top:10px}
.navbar{left:0;top:135px;width:1168px;height:45px;background:var(--navbar);color:#fff;font-size:16px}
.navbar .lang{left:100px;top:12px;display:flex;align-items:center;gap:6px}
.navbar .clock{left:275px;top:15px}
.tools{left:752px;top:11px;display:flex;align-items:center;gap:16px;font-size:16px}
.tools .sep{width:1px;height:24px;background:#4a5d63}

/* left column */
.box-head{background:var(--brand);color:#fff;font-size:16px;text-align:center}
.fav{left:100px;top:203px;width:211px;height:157px;background:var(--panel-gray)}
.fav .box-head{height:41px;padding-top:17px;text-align:left;padding-left:30px}
.fav .hint{margin:11px 6px 0 7px;height:67px;border:1px dashed var(--brand-mid);color:var(--brand-mid);font-size:14px;text-align:center;padding-top:14px;line-height:1.25}
.tabs{left:100px;top:368px;width:211px;height:34px;display:flex;font-size:14px;color:#fff}
.tabs .on{width:110px;background:var(--brand);padding:13px 0 0 29px}
.tabs .off{flex:1;background:var(--navbar);padding:14px 0 0 21px}
.sportlist{left:100px;top:418px;width:211px;list-style:none;background:var(--brand)}
.sportlist li{height:31.85px;display:flex;align-items:center;padding:0 14px 0 9px;color:#fff;font-weight:700;font-size:13.5px;border-bottom:1px solid var(--brand-line);letter-spacing:.3px}
.sportlist li:last-child{border-bottom:0}
.sportlist .ic{width:16px;height:16px;border:2px solid #fff;border-radius:50%;margin-right:11px}
.sportlist .n{margin-left:auto}
.mybets{left:100px;top:1068px;width:211px;height:164px;background:var(--panel-gray)}
.mybets .box-head{height:42px;padding-top:13px}
.refresh{text-align:center;color:var(--brand);font-size:14px;margin-top:6px}
.nopending{margin:19px 0 0 11px;width:179px;height:32px;background:var(--accent);color:var(--topbar);text-align:center;font-size:14px;padding-top:8px;letter-spacing:.4px}
.viewall{position:absolute;left:1px;bottom:0;width:208px;height:25px;background:var(--brand);color:#fff;text-align:center;font-size:13px;padding-top:5px}

/* odds panels */
.panel{left:324px;width:776px}
.panel-head{height:43px;background:var(--brand);color:#fff;position:relative;border-radius:3px 3px 0 0}
.panel-head .title{position:absolute;left:16px;top:9px;font-weight:700;font-size:15px;display:flex;align-items:center;gap:12px;letter-spacing:.5px}
.panel-head .count{position:absolute;left:333px;top:13px;font-size:17px}
.panel-head .league-pick{position:absolute;right:25px;top:13px;font-weight:700;font-size:14px;display:flex;gap:8px;align-items:center}
.grid{display:grid;grid-template-columns:69px 193px 50px 64px 60px 56px 70px 72px 66px 76px}
.colhead{height:54px;background:var(--brand-mid);color:#fff;font-size:14px;grid-template-rows:25px 29px}
.colhead div{display:flex;align-items:center;justify-content:center;border-right:1px solid var(--brand-line)}
.colhead .tall{grid-row:1/3}
.colhead .left{justify-content:flex-start;padding-left:11px}
.colhead .span4{grid-column:3/7;border-bottom:1px solid var(--brand-line);font-size:13px}
.colhead .span3{grid-column:7/10;border-bottom:1px solid var(--brand-line);font-size:13px}
.colhead .more{grid-column:10;grid-row:1/3;border-right:0}
.league{height:26px;background:var(--brand-dark);color:#fff;font-size:13px;display:flex;align-items:center;padding-left:34px;gap:8px;position:relative}
.league .pin{position:absolute;right:20px;top:6px}
.match{height:51px;background:var(--row);font-size:13px}
.match:nth-of-type(even){background:var(--row-alt)}
.match > div{border-right:1px solid var(--cell-line);position:relative}
.match .time{background:var(--time-cell)}
.match .stats{position:absolute;left:5px;bottom:9px;width:18px;height:18px;background:#6e7f84;border-radius:2px}
.match .time p{position:absolute;left:33px;top:13px;font-size:12px;color:#56666a;line-height:1.25}
.match .time em{color:var(--blue);font-style:italic}
.match .event{padding:11px 0 0 25px;font-weight:700;font-size:13.5px;line-height:1.2;letter-spacing:.3px}
.match .event .home{color:var(--home)}
.match .event .away{color:var(--away)}
.match .event .star{position:absolute;left:7px;top:18px;color:#889599;font-size:12px}
.odds{padding-top:8px;line-height:20px;font-size:13px}
.odds span{display:block}
.r{text-align:right;padding-right:10px}
.c{text-align:center}
.blue{color:var(--blue)}
.red{color:var(--red)}
.ou{font-size:11px;color:#56666a;text-align:center;padding-top:8px;line-height:20px}
.match .last{border-right:0;display:flex;align-items:center;padding-left:24px;gap:6px;font-size:13px}
.match .fh{border-right:0}
.match .fh.end{border-right:1px solid var(--cell-line)}

.footer{left:326px;top:1276px;font-size:12.5px;color:var(--muted);display:flex;gap:14px}
</style>
</head>
<body>
<div class="canvas">

  <header>
    <div class="abs topbar">
      <nav class="abs menu"><span>My Bets</span><span>Statements</span><span>Preferences</span><span>Announcements</span><span class="badge">99+</span></nav>
      <span class="abs user">Hi, stwtg036</span>
      <div class="abs wallet">» &nbsp;SD$ &nbsp;10,072.00 ↻</div>
      <div class="abs signout">Sign Out</div>
    </div>
    <div class="abs logo">LOGO</div>
    <div class="abs results">
      <svg width="24" height="16" viewBox="0 0 24 16" fill="#0f5566"><rect x="0" y="8" width="8" height="8"/><rect x="8" y="2" width="8" height="14"/><rect x="16" y="10" width="8" height="6"/></svg>
      Results
    </div>
    <div class="abs sports-tab">Sports</div>
    <div class="abs navbar">
      <div class="abs lang">
        <svg width="22" height="22" viewBox="0 0 22 22" fill="none" stroke="#fff" stroke-width="1.3"><circle cx="11" cy="11" r="9.5"/><ellipse cx="11" cy="11" rx="4" ry="9.5"/><path d="M2 11h18M3.5 6.5h15M3.5 15.5h15"/></svg>
        English (Asia) ▾
      </div>
      <div class="abs clock">12/02/2013 15:53 PM GMT +8</div>
      <div class="abs tools">
        <span>⊞ ▾</span><span class="sep"></span><span>★ ▾</span><span class="sep"></span><span>☰ ▾</span><span class="sep"></span><span>MY ▾</span><span class="sep"></span><span>◀)</span><span class="sep"></span><span>▭</span><span class="sep"></span><span>Live</span>
      </div>
    </div>
  </header>

  <aside>
    <section class="abs fav">
      <div class="box-head">My Favourites</div>
      <div class="hint">Click 0 an event or league<br>to add it to "My Favourites".</div>
    </section>
    <div class="abs tabs"><div class="on">Sports</div><div class="off">Markets</div></div>
    <ul class="abs sportlist">
      <li><i class="ic"></i>Football<span class="n">600</span></li>
      <li><i class="ic"></i>Basketball<span class="n">600</span></li>
      <li><i class="ic"></i>Baseball<span class="n">600</span></li>
      <li><i class="ic"></i>Tennis<span class="n">600</span></li>
      <li><i class="ic"></i>American Football<span class="n">600</span></li>
      <li><i class="ic"></i>Badminton<span class="n">600</span></li>
      <li><i class="ic"></i>Boxing<span class="n">600</span></li>
      <li><i class="ic"></i>Cricket<span class="n">600</span></li>
      <li><i class="ic"></i>Cycling<span class="n">600</span></li>
      <li><i class="ic"></i>Darts<span class="n">600</span></li>
      <li><i class="ic"></i>Entertainment<span class="n">600</span></li>
      <li><i class="ic"></i>Golf<span class="n">600</span></li>
      <li><i class="ic"></i>Handball<span class="n">600</span></li>
      <li><i class="ic"></i>Ice Hockey<span class="n">600</span></li>
      <li><i class="ic"></i>Mixed Martial Arts<span class="n">600</span></li>
      <li><i class="ic"></i>Motor Sport<span class="n">600</span></li>
      <li><i class="ic"></i>Pool Snooker<span class="n">600</span></li>
      <li><i class="ic"></i>Rugby<span class="n">600</span></li>
      <li><i class="ic"></i>Volleyball<span class="n">600</span></li>
      <li><i class="ic"></i>Winter Sport<span class="n">600</span></li>
    </ul>
    <section class="abs mybets">
      <div class="box-head">My Bets</div>
      <div class="refresh">↻ &nbsp;Refresh</div>
      <div class="nopending">No Pending bets</div>
      <div class="viewall">View All</div>
    </section>
  </aside>

  <main>
    <section class="abs panel" style="top:202px">
      <div class="panel-head">
        <div class="title"><svg width="26" height="26" viewBox="0 0 26 26"><circle cx="13" cy="13" r="10" fill="none" stroke="#fff" stroke-width="2"/></svg>Today - Live</div>
        <div class="count">↻ 38</div>
        <div class="league-pick"><svg width="18" height="18" viewBox="0 0 18 18" fill="#fff"><path d="M4 1h10v5a5 5 0 0 1-10 0zM8 11h2v3h3v3H5v-3h3z"/></svg>Select League</div>
      </div>
      <div class="grid colhead">
        <div class="tall left">Times</div><div class="tall">Event</div>
        <div class="span4">Full Time</div><div class="span3">First Half</div><div class="more">+More</div>
        <div>A1x2</div><div>HDP</div><div>OU</div><div>1x2</div><div>HDP</div><div>OU</div><div>1x2</div>
      </div>
      <div class="league">★ Coastal Premier League<span class="pin">↻</span></div>
      <div class="grid match"><div class="time"><i class="stats"></i><p>16:30<br><em>Live</em></p></div><div class="event"><span class="star">★</span><div class="home">Harbour City Mariners</div><div class="away">Southbank Victory</div></div><div class="odds"><span class="r">0.77</span><span class="blue" style="padding-left:14px">0-0.5</span></div><div class="odds c"><span class="blue">6-6.5</span><span class="red">-0.95</span></div><div class="ou">o<br>u</div><div class="odds c"><span class="red">-0.85</span><span>0.65</span></div><div class="fh"></div><div class="fh"></div><div class="fh end"></div><div class="last">⇕ 13</div></div>
    </section>

    <section class="abs panel" style="top:390px">
      <div class="panel-head">
        <div class="title"><svg width="26" height="26" viewBox="0 0 26 26"><circle cx="13" cy="13" r="10" fill="none" stroke="#fff" stroke-width="2"/></svg>Today - Non - Live</div>
        <div class="count">↻ 38</div>
        <div class="league-pick"><svg width="18" height="18" viewBox="0 0 18 18" fill="#fff"><path d="M4 1h10v5a5 5 0 0 1-10 0zM8 11h2v3h3v3H5v-3h3z"/></svg>Select League</div>
      </div>
      <div class="grid colhead">
        <div class="tall left">Times</div><div class="tall">Event</div>
        <div class="span4">Full Time</div><div class="span3">First Half</div><div class="more">+More</div>
        <div>A1x2</div><div>HDP</div><div>OU</div><div>1x2</div><div>HDP</div><div>OU</div><div>1x2</div>
      </div>

      <div class="league">★ Coastal Premier League<span class="pin">↻</span></div>
      <div class="grid match"><div class="time"><i class="stats"></i><p>16:30<br><em>Live</em></p></div><div class="event"><span class="star">★</span><div class="home">Harbour City Mariners</div><div class="away">Southbank Victory</div></div><div class="odds"><span class="r">0.77</span><span class="blue" style="padding-left:14px">0-0.5</span></div><div class="odds c"><span class="blue">6-6.5</span><span class="red">-0.95</span></div><div class="ou">o<br>u</div><div class="odds c"><span class="red">-0.85</span><span>0.65</span></div><div class="fh"></div><div class="fh"></div><div class="fh end"></div><div class="last">⇕ 13</div></div>

      <div class="league">★ Coastal Premier League<span class="pin">↻</span></div>
      <div class="grid match"><div class="time"><i class="stats"></i><p>16:30<br><em>Live</em></p></div><div class="event"><span class="star">★</span><div class="home">Harbour City Mariners</div><div class="away">Southbank Victory</div></div><div class="odds"><span class="r">0.77</span><span class="blue" style="padding-left:14px">0-0.5</span></div><div class="odds c"><span class="blue">6-6.5</span><span class="red">-0.95</span></div><div class="ou">o<br>u</div><div class="odds c"><span class="red">-0.85</span><span>0.65</span></div><div class="fh"></div><div class="fh"></div><div class="fh end"></div><div class="last">⇕ 13</div></div>
      <div class="grid match"><div class="time"><i class="stats"></i><p>16:30<br><em>Live</em></p></div><div class="event"><span class="star">★</span><div class="home">Harbour City Mariners</div><div class="away">Southbank Victory</div></div><div class="odds"><span class="r">0.77</span><span class="blue" style="padding-left:14px">0-0.5</span></div><div class="odds c"><span class="blue">6-6.5</span><span class="red">-0.95</span></div><div class="ou">o<br>u</div><div class="odds c"><span class="red">-0.85</span><span>0.65</span></div><div class="fh"></div><div class="fh"></div><div class="fh end"></div><div class="last">⇕ 13</div></div>
      <div class="grid match"><div class="time"><i class="stats"></i><p>16:30<br><em>Live</em></p></div><div class="event"><span class="star">★</span><div class="home">Harbour City Mariners</div><div class="away">Southbank Victory</div></div><div class="odds"><span class="r">0.77</span><span class="blue" style="padding-left:14px">0-0.5</span></div><div class="odds c"><span class="blue">6-6.5</span><span class="red">-0.95</span></div><div class="ou">o<br>u</div><div class="odds c"><span class="red">-0.85</span><span>0.65</span></div><div class="fh"></div><div class="fh"></div><div class="fh end"></div><div class="last">⇕ 13</div></div>

      <div class="league">★ Coastal Premier League<span class="pin">↻</span></div>
      <div class="grid match"><div class="time"><i class="stats"></i><p>16:30<br><em>Live</em></p></div><div class="event"><span class="star">★</span><div class="home">Harbour City Mariners</div><div class="away">Southbank Victory</div></div><div class="odds"><span class="r">0.77</span><span class="blue" style="padding-left:14px">0-0.5</span></div><div class="odds c"><span class="blue">6-6.5</span><span class="red">-0.95</span></div><div class="ou">o<br>u</div><div class="odds c"><span class="red">-0.85</span><span>0.65</span></div><div class="fh"></div><div class="fh"></div><div class="fh end"></div><div class="last">⇕ 13</div></div>

      <div class="league">★ Coastal Premier League<span class="pin">↻</span></div>
      <div class="grid match"><div class="time"><i class="stats"></i><p>16:30<br><em>Live</em></p></div><div class="event"><span class="star">★</span><div class="home">Harbour City Mariners</div><div class="away">Southbank Victory</div></div><div class="odds"><span class="r">0.77</span><span class="blue" style="padding-left:14px">0-0.5</span></div><div class="odds c"><span class="blue">6-6.5</span><span class="red">-0.95</span></div><div class="ou">o<br>u</div><div class="odds c"><span class="red">-0.85</span><span>0.65</span></div><div class="fh"></div><div class="fh"></div><div class="fh end"></div><div class="last">⇕ 13</div></div>
      <div class="grid match"><div class="time"><i class="stats"></i><p>16:30<br><em>Live</em></p></div><div class="event"><span class="star">★</span><div class="home">Harbour City Mariners</div><div class="away">Southbank Victory</div></div><div class="odds"><span class="r">0.77</span><span class="blue" style="padding-left:14px">0-0.5</span></div><div class="odds c"><span class="blue">6-6.5</span><span class="red">-0.95</span></div><div class="ou">o<br>u</div><div class="odds c"><span class="red">-0.85</span><span>0.65</span></div><div class="fh"></div><div class="fh"></div><div class="fh end"></div><div class="last">⇕ 13</div></div>
      <div class="grid match"><div class="time"><i class="stats"></i><p>16:30<br><em>Live</em></p></div><div class="event"><span class="star">★</span><div class="home">Harbour City Mariners</div><div class="away">Southbank Victory</div></div><div class="odds"><span class="r">0.77</span><span class="blue" style="padding-left:14px">0-0.5</span></div><div class="odds c"><span class="blue">6-6.5</span><span class="red">-0.95</span></div><div class="ou">o<br>u</div><div class="odds c"><span class="red">-0.85</span><span>0.65</span></div><div class="fh"></div><div class="fh"></div><div class="fh end"></div><div class="last">⇕ 13</div></div>
      <div class="grid match"><div class="time"><i class="stats"></i><p>16:30<br><em>Live</em></p></div><div class="event"><span class="star">★</span><div class="home">Harbour City Mariners</div><div class="away">Southbank Victory</div></div><div class="odds"><span class="r">0.77</span><span class="blue" style="padding-left:14px">0-0.5</span></div><div class="odds c"><span class="blue">6-6.5</span><span class="red">-0.95</span></div><div class="ou">o<br>u</div><div class="odds c"><span class="red">-0.85</span><span>0.65</span></div><div class="fh"></div><div class="fh"></div><div class="fh end"></div><div class="last">⇕ 13</div></div>
      <div class="grid match"><div class="time"><i class="stats"></i><p>16:30<br><em>Live</em></p></div><div class="event"><span class="star">★</span><div class="home">Harbour City Mariners</div><div class="away">Southbank Victory</div></div><div class="odds"><span class="r">0.77</span><span class="blue" style="padding-left:14px">0-0.5</span></div><div class="odds c"><span class="blue">6-6.5</span><span class="red">-0.95</span></div><div class="ou">o<br>u</div><div class="odds c"><span class="red">-0.85</span><span>0.65</span></div><div class="fh"></div><div class="fh"></div><div class="fh end"></div><div class="last">⇕ 13</div></div>
      <div class="grid match"><div class="time"><i class="stats"></i><p>16:30<br><em>Live</em></p></div><div class="event"><span class="star">★</span><div class="home">Harbour City Mariners</div><div class="away">Southbank Victory</div></div><div class="odds"><span class="r">0.77</span><span class="blue" style="padding-left:14px">0-0.5</span></div><div class="odds c"><span class="blue">6-6.5</span><span class="red">-0.95</span></div><div class="ou">o<br>u</div><div class="odds c"><span class="red">-0.85</span><span>0.65</span></div><div class="fh"></div><div class="fh"></div><div class="fh end"></div><div class="last">⇕ 13</div></div>
      <div class="grid match"><div class="time"><i class="stats"></i><p>16:30<br><em>Live</em></p></div><div class="event"><span class="star">★</span><div class="home">Harbour City Mariners</div><div class="away">Southbank Victory</div></div><div class="odds"><span class="r">0.77</span><span class="blue" style="padding-left:14px">0-0.5</span></div><div class="odds c"><span class="blue">6-6.5</span><span class="red">-0.95</span></div><div class="ou">o<br>u</div><div class="odds c"><span class="red">-0.85</span><span>0.65</span></div><div class="fh"></div><div class="fh"></div><div class="fh end"></div><div class="last">⇕ 13</div></div>
      <div class="grid match"><div class="time"><i class="stats"></i><p>16:30<br><em>Live</em></p></div><div class="event"><span class="star">★</span><div class="home">Harbour City Mariners</div><div class="away">Southbank Victory</div></div><div class="odds"><span class="r">0.77</span><span class="blue" style="padding-left:14px">0-0.5</span></div><div class="odds c"><span class="blue">6-6.5</span><span class="red">-0.95</span></div><div class="ou">o<br>u</div><div class="odds c"><span class="red">-0.85</span><span>0.65</span></div><div class="fh"></div><div class="fh"></div><div class="fh end"></div><div class="last">⇕ 13</div></div>
    </section>
  </main>

  <footer class="abs footer">
    <span>Betting Rule</span><span>|</span><span>Contact Us</span><span>|</span><span>Privacy Policy</span><span>|</span><span>Responsible Gambling</span><span>|</span><span>Terms &amp; Conditions</span><span>|</span><span>Tutorials</span>
  </footer>
</div>
</body>
</html>
```